Stretch on the Green with Mira

I want to advertise my Stretch on the Green classes for Summer. Classes are outside at the lovely local park. Holloway field. 83 Marangi St. Sandringham.
Classes are for beginners to advance levels.
Classes start Monday, October 17th.
Monday 6pm Beginners
Tuesday 6pm Intermediate
Thursday 6pm Intermediate/Advance
Saturday 9am All fitness levels
My Pilates classes are specially designed to help improve strength and flexibility but as well will also improve posture, reduce stress and develop control and endurance in the entire body.
Booking essential. Limited numbers so I can make sure the correct technique is always being followed.
For more info or to book contact details:
Mira 027358164
mira@corewithmira.net
www.corewithmira.net
$15 Per Session

Target Market(s)

Males and Females ages 35plus.

Industry/Entity Type

Fitness

Font styles to use
Sans Serif

Requirements
Must have
• My logo. Contact details. A Park that looks lovely to exercise at.
Nice to have
• Summer looking. Trees - inspiration to be exercising outside

```html
<!DOCTYPE html>
<html lang="en">
<head>
<meta charset="utf-8">
<title>Stretch on the Green with Mira</title>
<link rel="stylesheet" href="https://fonts.googleapis.com/css2?family=Oswald:wght@500;600;700&family=Rubik:wght@400;500;600&display=swap">
<style>
  :root {
    --pink: #f4589e;
    --pink-light: #ff86bd;
    --pink-deep: #ee3f8c;
    --green: #1f6b0c;
    --green-dark: #175a08;
    --ink: #1d1d1f;
    --text: #2a2a2a;
    --grey: #4a4a4c;
    --paper: #f7f7f7;
    --white: #ffffff;
  }
  * { margin: 0; padding: 0; box-sizing: border-box; }
  html, body { width: 990px; height: 1200px; overflow: hidden; background: var(--paper); }
  .flyer { position: relative; width: 990px; height: 1200px; overflow: hidden; background: var(--paper); font-family: "Rubik", sans-serif; }
  .flyer-art { position: absolute; inset: 0; }

  .brand { position: absolute; left: 87px; top: 112px; width: 435px; text-align: center; }
  .brand-mark { width: 46px; height: 46px; border-radius: 50%; background: #8d8d8d; margin: 0 auto 18px; }
  .brand-name { font-family: "Rubik", sans-serif; font-weight: 400; font-size: 34px; letter-spacing: 2px; text-transform: uppercase; color: var(--pink-light); white-space: nowrap; }

  .class-list { position: absolute; left: 73px; top: 768px; list-style: none; }
  .class-list li { position: relative; padding-left: 37px; font-weight: 600; font-size: 22.5px; line-height: 28px; color: var(--ink); margin-bottom: 14px; }
  .class-list li svg { position: absolute; left: 0; top: 4px; width: 22px; height: 22px; }

  .venue { position: absolute; left: 549px; top: 760px; width: 367px; }
  .venue-pin { display: block; margin: 0 auto -6px; width: 20px; height: 26px; position: relative; z-index: 2; }
  .venue-box { border: 2px solid var(--green); border-radius: 4px; overflow: hidden; font-family: "Oswald", sans-serif; font-weight: 500; text-align: center; white-space: nowrap; }
  .venue-tag { background: var(--white); color: var(--pink); font-size: 19px; letter-spacing: -0.3px; line-height: 38px; }
  .venue-address { background: var(--green); color: var(--white); font-size: 16.5px; letter-spacing: -0.2px; line-height: 36px; }

  .about { position: absolute; left: 549px; top: 886px; width: 367px; font-size: 13.4px; line-height: 20.5px; color: var(--text); text-align: justify; }
  .about p + p { margin-top: 14px; text-align: left; }

  .footer-band { position: absolute; left: 0; top: 1094px; width: 990px; height: 106px; background: linear-gradient(90deg, var(--pink-deep), var(--pink-light)); }
  .contact-pill { position: absolute; left: 148px; top: 1068px; width: 690px; height: 50px; border-radius: 25px; border: 2px solid var(--white); background: var(--green); display: flex; overflow: hidden; }
  .contact-label { flex: 1; color: var(--white); font-weight: 600; font-size: 20px; line-height: 46px; padding-left: 31px; white-space: nowrap; }
  .contact-name { width: 228px; background: var(--grey); color: var(--white); font-weight: 600; font-size: 20px; line-height: 46px; text-align: center; border-radius: 25px; border-left: 2px solid var(--white); white-space: nowrap; }
  .contact-row { position: absolute; left: 73px; top: 1134px; display: flex; align-items: center; color: var(--white); font-weight: 500; font-size: 20px; white-space: nowrap; }
  .contact-row span { display: flex; align-items: center; gap: 8px; }
  .contact-row svg { width: 18px; height: 18px; }
  .divider { margin: 0 30px; }
</style>
</head>
<body>
<div class="flyer">
  <svg class="flyer-art" viewBox="0 0 990 1200" width="990" height="1200">
    <defs>
      <linearGradient id="park-tones" x1="0" y1="0" x2="0" y2="1">
        <stop offset="0" stop-color="#eef0ec"/>
        <stop offset="0.35" stop-color="#b7c8ac"/>
        <stop offset="0.48" stop-color="#6f9a55"/>
        <stop offset="0.58" stop-color="#a7b4ae"/>
        <stop offset="0.72" stop-color="#7fa66a"/>
        <stop offset="0.85" stop-color="#4f8d2c"/>
        <stop offset="1" stop-color="#3f7a22"/>
      </linearGradient>
      <linearGradient id="sky-fade" x1="0" y1="0" x2="1" y2="1">
        <stop offset="0" stop-color="#f7f7f7"/>
        <stop offset="0.45" stop-color="#f7f7f7" stop-opacity="0.6"/>
        <stop offset="0.7" stop-color="#f7f7f7" stop-opacity="0"/>
      </linearGradient>
      <linearGradient id="headline-fill" x1="0" y1="0" x2="0" y2="1">
        <stop offset="0" stop-color="#f4589e"/>
        <stop offset="0.7" stop-color="#ff8cc2"/>
        <stop offset="1" stop-color="#ff8cc2" stop-opacity="0.35"/>
      </linearGradient>
      <linearGradient id="wave-fill" x1="0" y1="0" x2="1" y2="0">
        <stop offset="0" stop-color="#ff8cc2"/>
        <stop offset="1" stop-color="#f2448f"/>
      </linearGradient>
      <linearGradient id="ring-fill" x1="0" y1="0" x2="1" y2="1">
        <stop offset="0" stop-color="#5a5a5c"/>
        <stop offset="0.35" stop-color="#f2f2f2"/>
        <stop offset="0.6" stop-color="#9b9b9d"/>
        <stop offset="1" stop-color="#3c3c3e"/>
      </linearGradient>
      <linearGradient id="badge-fill" x1="0" y1="0" x2="0" y2="1">
        <stop offset="0" stop-color="#ff6fae"/>
        <stop offset="1" stop-color="#ff8cc2"/>
      </linearGradient>
    </defs>

    <g role="img" aria-label="Photo: a woman seated cross-legged on park grass beside a lake, arms raised overhead, trees behind">
      <rect x="0" y="150" width="990" height="600" fill="url(#park-tones)"/>
      <rect x="0" y="150" width="990" height="300" fill="url(#sky-fade)"/>
    </g>

    <rect x="89" y="233" width="357" height="82" fill="var(--pink)"/>
    <text x="267" y="302" text-anchor="middle" font-family="Oswald, sans-serif" font-weight="600" font-size="66" letter-spacing="9" fill="#fff">STRETCH</text>

    <text x="87" y="458" textLength="815" lengthAdjust="spacingAndGlyphs" font-family="Oswald, sans-serif" font-weight="600" font-size="168" fill="url(#headline-fill)">ON THE GREEN</text>

    <path d="M0,668 C110,600 250,590 380,630 C560,690 800,750 990,548 L990,585 C800,770 560,748 400,700 C270,660 130,650 0,700 Z" fill="url(#wave-fill)"/>
    <path d="M0,700 C130,650 270,660 400,700 C560,748 800,770 990,585 L990,1200 L0,1200 Z" fill="var(--paper)"/>

    <circle cx="219" cy="611" r="128" fill="none" stroke="var(--pink-light)" stroke-width="1.5"/>
    <path d="M99,611 A120,120 0 1 1 339,611 L339,731 L219,731 A120,120 0 0 1 99,611 Z" fill="url(#ring-fill)"/>
    <circle cx="219" cy="611" r="104" fill="url(#badge-fill)"/>
    <text x="219" y="640" text-anchor="middle" font-family="Oswald, sans-serif" font-weight="700" font-size="84" fill="#fff">$15</text>
    <text x="219" y="676" text-anchor="middle" font-family="Oswald, sans-serif" font-weight="500" font-size="27" fill="#fff">PER SESSION</text>
  </svg>

  <div class="brand">
    <div class="brand-mark"></div>
    <div class="brand-name">Core with Mira</div>
  </div>

  <ul class="class-list">
    <li><svg viewBox="0 0 22 22"><circle cx="11" cy="11" r="9.5" fill="none" stroke="#f4589e" stroke-width="1.6"/><path d="M6.5 11.2l3 3 6-6" fill="none" stroke="#f4589e" stroke-width="1.6"/></svg>Classes are for<br>beginners to advance levels.</li>
    <li><svg viewBox="0 0 22 22"><circle cx="11" cy="11" r="9.5" fill="none" stroke="#f4589e" stroke-width="1.6"/><path d="M6.5 11.2l3 3 6-6" fill="none" stroke="#f4589e" stroke-width="1.6"/></svg>Classes start Monday, October 17th.</li>
    <li><svg viewBox="0 0 22 22"><circle cx="11" cy="11" r="9.5" fill="none" stroke="#f4589e" stroke-width="1.6"/><path d="M6.5 11.2l3 3 6-6" fill="none" stroke="#f4589e" stroke-width="1.6"/></svg>Monday 6pm Beginners</li>
    <li><svg viewBox="0 0 22 22"><circle cx="11" cy="11" r="9.5" fill="none" stroke="#f4589e" stroke-width="1.6"/><path d="M6.5 11.2l3 3 6-6" fill="none" stroke="#f4589e" stroke-width="1.6"/></svg>Tuesday 6pm Intermediate</li>
    <li><svg viewBox="0 0 22 22"><circle cx="11" cy="11" r="9.5" fill="none" stroke="#f4589e" stroke-width="1.6"/><path d="M6.5 11.2l3 3 6-6" fill="none" stroke="#f4589e" stroke-width="1.6"/></svg>Thursday 6pm Intermediate/Advance</li>
    <li><svg viewBox="0 0 22 22"><circle cx="11" cy="11" r="9.5" fill="none" stroke="#f4589e" stroke-width="1.6"/><path d="M6.5 11.2l3 3 6-6" fill="none" stroke="#f4589e" stroke-width="1.6"/></svg>Saturday 9am All fitness levels</li>
  </ul>

  <div class="venue">
    <svg class="venue-pin" viewBox="0 0 20 26"><rect x="0" y="4" width="20" height="20" fill="var(--paper)"/><circle cx="10" cy="7" r="5" fill="none" stroke="#1f6b0c" stroke-width="2.2"/><path d="M10 12v8" stroke="#1f6b0c" stroke-width="2.2"/><ellipse cx="10" cy="21" rx="7" ry="2.5" fill="none" stroke="#1f6b0c" stroke-width="1.5"/></svg>
    <div class="venue-box">
      <div class="venue-tag">A PARK THAT LOOKS LOVELY TO EXERCISE AT.</div>
      <div class="venue-address">HOLLOWAY FIELD. 83 MARANGI ST. SANDRINGHAM</div>
    </div>
  </div>

  <div class="about">
    <p>My Pilates classes are specially designed to help improve strength and flexibility but as well will also improve posture, reduce stress and develop control and endurance in the entire body.</p>
    <p>Booking essential. Limited numbers so I can make sure the correct technique is always being followed.</p>
  </div>

  <div class="footer-band"></div>
  <div class="contact-pill">
    <div class="contact-label">FOR MORE INFO OR TO BOOK CONTACT :</div>
    <div class="contact-name">MIRA HALVORSEN</div>
  </div>
  <div class="contact-row">
    <span><svg viewBox="0 0 18 18"><circle cx="9" cy="9" r="8" fill="none" stroke="#fff" stroke-width="1.4"/><path d="M6 5.5l1.6-.4 1 2.2-1 .8a5 5 0 0 0 2.3 2.3l.8-1 2.2 1-.4 1.6c-3.4.3-6.8-3.1-6.5-6.5z" fill="#fff"/></svg>027358164</span>
    <span class="divider">|</span>
    <span><svg viewBox="0 0 18 18"><rect x="1.5" y="4" width="15" height="10" fill="none" stroke="#fff" stroke-width="1.4"/><path d="M1.5 4l7.5 6 7.5-6" fill="none" stroke="#fff" stroke-width="1.4"/></svg>mira@corewithmira.net</span>
    <span class="divider">|</span>
    <span><svg viewBox="0 0 18 18"><circle cx="9" cy="9" r="8" fill="none" stroke="#fff" stroke-width="1.4"/><ellipse cx="9" cy="9" rx="3.5" ry="8" fill="none" stroke="#fff" stroke-width="1.2"/><path d="M1 9h16M2.5 5h13M2.5 13h13" stroke="#fff" stroke-width="1.2"/></svg>www.corewithmira.net</span>
  </div>
</div>
</body>
</html>
```